Awesome business card design needed

We need a new business card design to go with our new logo.
We are a web development agency that specialises in highly complex back-end integrations as opposed to design, our customers are retailers, hotels, hospitals and any other organisation that has a large online marketing department.
Take a look at our website - www.orvekplus.com for some inspiration.
We want our new business cards to exude class, professionalism and style.
We are likely to choose a high-end card to print them on but we want the design of the card itself to really turn heads.
We have no specific colour requirements, the logo as you will see is a turquoise colour R89 G171 B167 #59aba7 but it can also be in white if you want to make the colour of the card something different.
The information on the card should be:
Name
Position
Tel
email
Potentially a double sided card could have our web address, twitter and FB links.

```html
<!DOCTYPE html>
<html lang="en">
<head>
<meta charset="utf-8">
<title>orvekplus business cards</title>
<link rel="stylesheet" href="https://fonts.googleapis.com/css2?family=Saira:wght@400;600;700&display=swap">
<style>
  :root {
    --backdrop: #1f1f1f;
    --teal: #59aba7;
    --teal-deep: #4a9894;
    --ink: #0a0a0a;
  }
  * { box-sizing: border-box; margin: 0; padding: 0; }
  html, body { width: 1200px; height: 900px; overflow: hidden; }
  body {
    background: var(--backdrop);
    font-family: "Saira", "Arial", sans-serif;
    position: relative;
  }
  .card {
    position: absolute;
    top: 300px;
    width: 525px;
    height: 300px;
    overflow: hidden;
    box-shadow: 0 10px 24px rgba(0,0,0,0.55);
  }
  /* Front side */
  .card--front { left: 40px; background: var(--ink); }
  .front__wordmark {
    position: absolute;
    left: 38px;
    top: 26px;
    font-weight: 700;
    font-size: 80px;
    line-height: 1;
    letter-spacing: 2px;
    color: var(--teal);
  }
  .front__pattern {
    position: absolute;
    left: 0;
    right: 0;
    bottom: 0;
    height: 150px;
    background: linear-gradient(to bottom, var(--teal) 0%, var(--teal-deep) 55%, rgba(74,152,148,0.35) 100%);
  }
  /* Back side */
  .card--back { left: 635px; background: var(--teal); }
  .back__nameplate {
    position: absolute;
    left: 0;
    top: 78px;
    width: 205px;
    height: 44px;
    background: var(--ink);
    border-radius: 0 7px 7px 0;
    padding: 5px 0 0 18px;
    color: var(--teal);
  }
  .nameplate__name {
    font-weight: 600;
    font-size: 14px;
    letter-spacing: 1px;
    line-height: 1.2;
  }
  .nameplate__role {
    font-size: 11px;
    line-height: 1.2;
  }
  .back__wordmark {
    position: absolute;
    right: 34px;
    top: 62px;
    font-weight: 700;
    font-size: 44px;
    line-height: 1;
    letter-spacing: 1px;
    color: var(--ink);
  }
  .back__contacts {
    position: absolute;
    right: 22px;
    top: 162px;
    list-style: none;
  }
  .contact {
    display: flex;
    justify-content: flex-end;
    align-items: center;
    gap: 8px;
    height: 22px;
    font-size: 13px;
    letter-spacing: 0.6px;
    color: var(--ink);
  }
  .contact--phone { font-weight: 600; }
  .contact__icon { width: 15px; height: 15px; flex: none; }
</style>
</head>
<body>

  <section class="card card--front" aria-label="Card front">
    <div class="front__wordmark">orvekplus</div>
    <div class="front__pattern" role="img" aria-label="Pixel-block mirror pattern of the brand name"></div>
  </section>

  <section class="card card--back" aria-label="Card back">
    <div class="back__nameplate">
      <div class="nameplate__name">LENA MARSH</div>
      <div class="nameplate__role">Customer Service</div>
    </div>

    <div class="back__wordmark">orvekplus</div>

    <ul class="back__contacts">
      <li class="contact contact--phone">555.014.2290
        <svg class="contact__icon" viewBox="0 0 16 16" aria-hidden="true">
          <circle cx="8" cy="8" r="7" fill="none" stroke="#0a0a0a" stroke-width="1.2"/>
          <path d="M5.6 4.6c.5-.3.8 0 1 .4l.5 1c.1.3 0 .6-.3.8l-.4.3c.3.8.9 1.6 1.7 2.1l.4-.3c.3-.2.6-.2.8 0l.9.7c.3.3.3.7 0 1l-.5.5c-1.9.6-5.5-3-4.7-5.9z" fill="#0a0a0a"/>
        </svg>
      </li>
      <li class="contact">lena@orvekplus.com
        <svg class="contact__icon" viewBox="0 0 16 16" aria-hidden="true">
          <circle cx="8" cy="8" r="7" fill="none" stroke="#0a0a0a" stroke-width="1.2"/>
          <rect x="4.5" y="5.5" width="7" height="5" fill="none" stroke="#0a0a0a" stroke-width="1"/>
          <path d="M4.5 5.5 8 8.3l3.5-2.8" fill="none" stroke="#0a0a0a" stroke-width="1"/>
        </svg>
      </li>
      <li class="contact">www.orvekplus.com
        <svg class="contact__icon" viewBox="0 0 16 16" aria-hidden="true">
          <circle cx="8" cy="8" r="7" fill="none" stroke="#0a0a0a" stroke-width="1.2"/>
          <circle cx="8" cy="8" r="3.6" fill="none" stroke="#0a0a0a" stroke-width="0.9"/>
          <path d="M4.4 8h7.2M8 4.4c-1.4 1.9-1.4 5.3 0 7.2M8 4.4c1.4 1.9 1.4 5.3 0 7.2" fill="none" stroke="#0a0a0a" stroke-width="0.8"/>
        </svg>
      </li>
      <li class="contact">social.orvekplus.com
        <svg class="contact__icon" viewBox="0 0 16 16" aria-hidden="true">
          <circle cx="8" cy="8" r="7" fill="none" stroke="#0a0a0a" stroke-width="1.2"/>
        </svg>
      </li>
      <li class="contact">@orvekplus
        <svg class="contact__icon" viewBox="0 0 16 16" aria-hidden="true">
          <circle cx="8" cy="8" r="7" fill="none" stroke="#0a0a0a" stroke-width="1.2"/>
        </svg>
      </li>
    </ul>
  </section>

</body>
</html>
```